RK Bastone Construction Inc.

Design a new business card for our construction company
To be removed from current card:
Delete 25 years
Delete Tenant fit up Renovations section

```html
<!DOCTYPE html>
<html lang="en">
<head>
<meta charset="UTF-8">
<title>RK Bastone Construction Inc. – Business Card</title>
<link rel="stylesheet" href="https://fonts.googleapis.com/css2?family=Lexend:wght@300;400;500&display=swap">
<style>
  :root {
    --backdrop: #46305f;
    --card-white: #ffffff;
    --brand-green: #13756a;
    --brand-purple: #43206e;
    --ink-purple: #4a2779;
    --text-light: #ffffff;
  }
  * { box-sizing: border-box; margin: 0; padding: 0; }
  html, body {
    width: 1200px; height: 900px; overflow: hidden;
    background: var(--backdrop);
    font-family: "Lexend", sans-serif;
  }
  .canvas {
    position: relative; width: 1200px; height: 900px;
  }
  .card {
    position: absolute; top: 295px;
    width: 525px; height: 300px;
    overflow: hidden;
    box-shadow: 0 18px 40px rgba(15, 5, 30, 0.45);
  }

  /* Front */
  .card-front { left: 55px; background: var(--card-white); color: var(--ink-purple); }
  .accent-square {
    position: absolute; left: -14px; top: 34px;
    width: 52px; height: 44px; background: var(--brand-green);
  }
  .services {
    position: absolute; left: 62px; top: 30px;
    font-size: 13px; font-weight: 300; line-height: 17px;
  }
  .services .divider { color: var(--brand-green); margin: 0 3px; }
  .front-wordmark {
    position: absolute; right: 28px; top: 34px;
    font-size: 17px; font-weight: 500; letter-spacing: 0.5px;
    text-transform: uppercase; color: var(--ink-purple);
    text-align: right; line-height: 20px;
  }
  .person-name {
    position: absolute; left: 150px; top: 108px;
    font-size: 30px; font-weight: 400;
  }
  .person-mobile {
    position: absolute; left: 165px; top: 152px;
    display: flex; align-items: center; gap: 8px;
    font-size: 15px; font-weight: 300;
  }
  .contact-list {
    position: absolute; left: 24px; top: 196px;
    list-style: none;
  }
  .contact-item {
    display: flex; align-items: center; gap: 12px;
    font-size: 15px; font-weight: 300; height: 28px;
  }
  .icon { width: 18px; height: 18px; flex: none; }

  /* Back */
  .card-back { left: 620px; background: var(--brand-green); color: var(--text-light); }
  .back-wordmark {
    position: absolute; left: 0; right: 0; top: 72px;
    text-align: center; font-weight: 500; text-transform: uppercase;
    color: var(--text-light);
    font-size: 38px; letter-spacing: 1px; line-height: 44px;
  }
  .web-band {
    position: absolute; left: 0; right: 0; top: 218px; height: 40px;
    background: var(--brand-purple);
    display: flex; align-items: center; justify-content: center; gap: 12px;
    font-size: 16px; font-weight: 300;
  }
</style>
</head>
<body>
<main class="canvas">

  <section class="card card-front" aria-label="Business card front">
    <div class="accent-square"></div>
    <p class="services">
      Turn Key Operations<br>
      Project Management<br>
      Office<span class="divider">|</span>Retail<span class="divider">|</span>Institutional
    </p>
    <p class="front-wordmark">RK Bastone<br>Construction Inc.</p>

    <h1 class="person-name">Luc Bastone</h1>
    <p class="person-mobile">
      <svg class="icon" viewBox="0 0 18 18" aria-hidden="true">
        <circle cx="9" cy="9" r="9" fill="var(--brand-green)"/>
        <rect x="6" y="4" width="6" height="10" rx="1" fill="none" stroke="#fff" stroke-width="1.2"/>
      </svg>
      555-214-3078
    </p>

    <ul class="contact-list">
      <li class="contact-item">
        <svg class="icon" viewBox="0 0 18 18" aria-hidden="true">
          <circle cx="9" cy="9" r="9" fill="var(--brand-green)"/>
          <rect x="4.5" y="5.5" width="9" height="7" fill="none" stroke="#fff" stroke-width="1.1"/>
          <path d="M4.5 5.5 L9 9.5 L13.5 5.5 M4.5 12.5 L8 9 M13.5 12.5 L10 9" fill="none" stroke="#fff" stroke-width="1.1"/>
        </svg>
        luc@rkbastoneconst.ca
      </li>
      <li class="contact-item">
        <svg class="icon" viewBox="0 0 18 18" aria-hidden="true">
          <circle cx="9" cy="9" r="9" fill="var(--brand-green)"/>
          <rect x="6" y="4" width="6" height="10" rx="1" fill="none" stroke="#fff" stroke-width="1.2"/>
        </svg>
        555-630-4412&nbsp; ext : 118
      </li>
      <li class="contact-item">
        <svg class="icon" viewBox="0 0 18 18" aria-hidden="true">
          <path d="M9 17 C5 12 3.5 9.5 3.5 7 A5.5 5.5 0 0 1 14.5 7 C14.5 9.5 13 12 9 17 Z" fill="var(--brand-green)"/>
          <circle cx="9" cy="7" r="2" fill="#fff"/>
        </svg>
        2180 Fernbrook Ave., Suite 200, Kingsfield, ON K9Z 4B7
      </li>
    </ul>
  </section>

  <section class="card card-back" aria-label="Business card back">
    <p class="back-wordmark">RK Bastone<br>Construction Inc.</p>
    <div class="web-band">
      <svg class="icon" viewBox="0 0 20 20" aria-hidden="true" style="width:20px;height:20px">
        <circle cx="10" cy="10" r="9" fill="none" stroke="#fff" stroke-width="1.3"/>
        <ellipse cx="10" cy="10" rx="4" ry="9" fill="none" stroke="#fff" stroke-width="1"/>
        <path d="M1 10 H19 M2.5 5.5 H17.5 M2.5 14.5 H17.5" stroke="#fff" stroke-width="1"/>
      </svg>
      www.rkbastoneconstruction.ca
    </div>
  </section>

</main>
</body>
</html>
```